Business Card Design

We are a commercial real estate brokerage in San Francisco, leasing office buildings downtown.
I would like a clean, elegant look. Simple but powerful .

Industry/Entity Type

Business

Contact Information for Business Card

Colin Farrow
lic# 07281549
415.555.0172
colin@tarvo-commercial.example
tarvo-commercial.example

```html
<!DOCTYPE html>
<html lang="en">
<head>
<meta charset="utf-8">
<title>Tarvo Commercial – Business Card</title>
<link rel="stylesheet" href="https://fonts.googleapis.com/css2?family=Jost:wght@400;500&display=swap">
<style>
  :root {
    --page-bg: #d9d6d2;
    --card-bg: #151515;
    --accent: #8f9bb3;
    --muted: #6f747c;
    --rule: #2c2c2e;
    --mark: #3a3b3f;
  }
  * { margin: 0; padding: 0; box-sizing: border-box; }
  html, body {
    width: 1200px; height: 900px; overflow: hidden;
    background: var(--page-bg);
    font-family: "Jost", "Futura", sans-serif;
  }
  .card {
    position: absolute; left: 100px; top: 164px;
    width: 1000px; height: 572px;
    background: var(--card-bg);
    box-shadow: 0 18px 40px rgba(0,0,0,.25);
  }
  .agent { position: absolute; left: 110px; top: 172px; }
  .agent-name {
    color: var(--accent); font-weight: 500; font-size: 25px;
    letter-spacing: .5px; text-transform: uppercase; line-height: 1.1;
  }
  .agent-license { color: var(--muted); font-size: 24px; line-height: 1.15; }
  .divider {
    position: absolute; left: 110px; right: 110px; top: 262px;
    height: 1px; background: var(--rule);
  }
  .contacts { position: absolute; left: 110px; top: 292px; list-style: none; }
  .contacts li {
    display: flex; align-items: center; gap: 18px;
    color: var(--muted); font-size: 25px; height: 44px;
  }
  .contacts svg { width: 22px; height: 22px; fill: none; stroke: var(--muted); stroke-width: 1.6; }
  .contacts .icon-phone { fill: var(--muted); stroke: none; }
  .brand {
    position: absolute; right: 110px; top: 150px;
    display: flex; align-items: center; gap: 24px;
  }
  .brand-square { width: 110px; height: 110px; background: var(--mark); }
  .brand-name {
    color: var(--accent); font-weight: 500; text-transform: uppercase;
    line-height: .95;
  }
  .brand-name .primary { display: block; font-size: 74px; letter-spacing: 2px; }
  .brand-name .secondary { display: block; font-size: 31px; letter-spacing: 2px; }
</style>
</head>
<body>
  <main class="card">
    <section class="agent">
      <p class="agent-name">Colin Farrow</p>
      <p class="agent-license">lic# 07281549</p>
    </section>

    <div class="divider"></div>

    <ul class="contacts">
      <li>
        <svg viewBox="0 0 24 24" class="icon-phone"><path d="M6.6 2.5c.6-.3 1.3 0 1.6.6l1.6 3.4c.3.6.1 1.2-.4 1.6l-1.6 1.2c.9 2.3 2.6 4.5 4.6 5.9l1.5-1.3c.5-.4 1.2-.4 1.7 0l2.9 2.3c.5.4.6 1.1.2 1.7l-1.4 2c-.5.7-1.4 1-2.2.7C9.2 18.6 4.9 13.6 3.9 7.5c-.1-.8.2-1.6.9-2z"/></svg>
        <span>415.555.0172</span>
      </li>
      <li>
        <svg viewBox="0 0 24 24"><rect x="2.5" y="5.5" width="19" height="13"/><path d="M2.5 5.5 12 13l9.5-7.5"/></svg>
        <span>colin@tarvo-commercial.example</span>
      </li>
      <li>
        <svg viewBox="0 0 24 24"><circle cx="12" cy="12" r="9.5"/><ellipse cx="12" cy="12" rx="4" ry="9.5"/><path d="M2.5 12h19M4 7h16M4 17h16"/></svg>
        <span>tarvo-commercial.example</span>
      </li>
    </ul>

    <div class="brand">
      <div class="brand-square"></div>
      <p class="brand-name"><span class="primary">Tarvo</span><span class="secondary">Commercial</span></p>
    </div>
  </main>
</body>
</html>
```